Advertising plattform for handcraft companies

We need as design for an advertising platform for handcraft companies. The central element of the design should be a grid of 9 visible (but scrollables) boxes. In this boxes are logos of the advertising companies are shown.
Clicking a box will open es small window (like a lightbox) with further information about the company.

The main page will show a grid with the nine states of Austria. Clicking a state will show a grid with companies of this state sorted by region. Every region are represented in on line (3 boxes).

The design should be realizable as "responsive design".

Target Market(s)

- Austria
- for all customers who are looking for a plumber

Industry/Entity Type

Advertising

Requirements
Must have
• - Details shown as "lightbox"
• - Middle strip in "Companies" page should be highlighted
• - up and down scrolling funtionaltiy for "Companies" grid
• - Companies are selectable by state and region with drowdown menus (selected region will be highlighted)
• - Screen should show the elements as shown in the uploaded sketches.
Nice to have
• - Interesting wallpaper (website will advertise plumbers)
• - Nice animated effects

```html
<!DOCTYPE html>
<html lang="de">
<head>
<meta charset="utf-8">
<title>ROHRWERK.at – Handwerksbetriebe in Österreich</title>
<link href="https://fonts.googleapis.com/css2?family=Raleway:wght@400;500;600;700&display=swap" rel="stylesheet">
<style>
  :root{
    --brand-red:#bf1e24;
    --page-bg:#e5e5e7;
    --text-dark:#3a3a3a;
    --tile-bg:#f4f1ee;
    --tile-frame:#f7f5f3;
    --tile-line:#e2ddd8;
    --corner:#d6d4d3;
    --corner-text:#4a4a4a;
    --footer-bg:#3c3837;
    --footer-text:#f1f1f1;
    --footer-muted:#bdbab8;
    --icon-bg:#77726f;
  }
  *{box-sizing:border-box;margin:0;padding:0}
  html,body{width:1163px;height:1200px;overflow:hidden}
  body{font-family:'Raleway',sans-serif;background:var(--page-bg);color:var(--text-dark);position:relative}

  .site-header{position:absolute;left:0;top:0;width:1163px;height:101px;background:var(--brand-red)}
  .site-header::after{content:"";position:absolute;left:0;top:101px;width:100%;height:5px;
    background:radial-gradient(circle at 5px 0,var(--brand-red) 4px,transparent 4.5px) 0 0/10px 5px repeat-x}
  .brand{position:absolute;left:201px;top:38px;display:flex;align-items:center;gap:5px;
    color:#fff;font-weight:500;font-size:23px;letter-spacing:.2px}
  .brand-mark{width:25px;height:25px;background:#3a3636;border-radius:3px}
  .main-nav{position:absolute;left:764px;top:38px;display:flex;font-size:12.5px;font-weight:500}
  .main-nav a{color:#fff;text-decoration:none;height:27px;line-height:27px;padding:0 9px;margin-right:5px}
  .main-nav a.is-active{background:#f2f2f2;color:var(--brand-red);border-radius:3px}
  .main-nav a + a{margin-left:2px}

  .intro{position:absolute;left:150px;top:134px;width:863px;text-align:center}
  .intro h1{font-weight:500;font-size:28px;letter-spacing:.2px;color:var(--text-dark)}
  .intro p{margin-top:11px;font-size:14px;line-height:25px;letter-spacing:.4px;color:#444}

  .state-grid{position:absolute;left:283px;top:284px;width:600px;height:600px}
  .state-tile{position:absolute;width:176px;height:176px;background:var(--tile-frame);
    box-shadow:0 0 6px rgba(0,0,0,.06)}
  .state-tile .inner{position:absolute;left:7px;top:7px;right:7px;bottom:7px;background:var(--tile-bg);
    border:1px solid var(--tile-line);overflow:hidden}
  .state-name{position:absolute;left:0;right:0;top:76px;text-align:center;color:var(--brand-red);
    font-weight:700;font-size:15.5px;letter-spacing:.6px;line-height:18px}
  .corner{position:absolute;right:0;bottom:0;width:75px;height:75px}
  .corner-label{font-family:Arial,sans-serif;font-size:9px;fill:var(--corner-text)}

  .site-footer{position:absolute;left:0;top:954px;width:1163px;height:246px;background:var(--footer-bg);color:var(--footer-text)}
  .site-footer::before{content:"";position:absolute;left:0;top:-5px;width:100%;height:5px;
    background:radial-gradient(circle at 5px 5px,var(--footer-bg) 4px,transparent 4.5px) 0 0/10px 5px repeat-x}
  .footer-col{position:absolute;top:49px}
  .footer-col h3{font-size:12px;font-weight:700;letter-spacing:-.1px}
  .link-list{list-style:none;margin-top:10px}
  .link-list li{font-size:12px;height:25px;line-height:25px;padding-left:12px;position:relative}
  .link-list li::before{content:"";position:absolute;left:1px;top:9px;border-left:4px solid #8d8986;
    border-top:3.5px solid transparent;border-bottom:3.5px solid transparent}
  .social-list{list-style:none;margin-top:11px}
  .social-list li{display:flex;align-items:center;gap:6px;height:30px;font-size:12.5px}
  .social-icon{width:26px;height:26px;border-radius:50%;background:var(--icon-bg)}
  .copyright{position:absolute;left:719px;top:205px;font-size:9px;color:var(--footer-muted)}
</style>
</head>
<body>
  <header class="site-header">
    <div class="brand"><span>ROHRWERK.at</span><span class="brand-mark"></span></div>
    <nav class="main-nav">
      <a href="#" class="is-active">HOME</a>
      <a href="#">IMPRIST</a>
      <a href="#">CONTACT</a>
    </nav>
  </header>

  <section class="intro">
    <h1>WELCOME TO ROHRWERK.AT</h1>
    <p>Lorem ipsum dolor sit amet, consectetur adipiscing elit. Sed quis nisi euismod, fermentum tellus a, lobortis quam.<br>Vestibulum condimentum mi vitae diam tristique, egestas dignissim diam mattis. Curabitur vel diam in massa<br>porttitor dictum id in lorem. Vivamus faucibus ac leo ac dignissim.</p>
  </section>

  <svg width="0" height="0" style="position:absolute">
    <defs>
      <symbol id="click-corner" viewBox="0 0 75 75">
        <polygon points="75,0 75,75 0,75" fill="#d6d4d3"/>
        <text class="corner-label" x="47" y="47" transform="rotate(-45 47 47)" text-anchor="middle" dominant-baseline="middle">CLICK</text>
        <text class="corner-label" x="55" y="56" transform="rotate(-45 55 56)" text-anchor="middle" dominant-baseline="middle">HERE</text>
      </symbol>
    </defs>
  </svg>

  <main class="state-grid">
    <a class="state-tile" style="left:0;top:0"><div class="inner"><div class="state-name">Burgenland</div><svg class="corner"><use href="#click-corner"/></svg></div></a>
    <a class="state-tile" style="left:213px;top:0"><div class="inner"><div class="state-name">Kärnten</div><svg class="corner"><use href="#click-corner"/></svg></div></a>
    <a class="state-tile" style="left:426px;top:0"><div class="inner"><div class="state-name">Niederösterreich</div><svg class="corner"><use href="#click-corner"/></svg></div></a>
    <a class="state-tile" style="left:0;top:211px"><div class="inner"><div class="state-name">Oberösterreich</div><svg class="corner"><use href="#click-corner"/></svg></div></a>
    <a class="state-tile" style="left:213px;top:211px"><div class="inner"><div class="state-name">Salzburg Land</div><svg class="corner"><use href="#click-corner"/></svg></div></a>
    <a class="state-tile" style="left:426px;top:211px"><div class="inner"><div class="state-name">Steiermark</div><svg class="corner"><use href="#click-corner"/></svg></div></a>
    <a class="state-tile" style="left:0;top:425px"><div class="inner"><div class="state-name">Tirol</div><svg class="corner"><use href="#click-corner"/></svg></div></a>
    <a class="state-tile" style="left:213px;top:425px"><div class="inner"><div class="state-name">Vorarlberg</div><svg class="corner"><use href="#click-corner"/></svg></div></a>
    <a class="state-tile" style="left:426px;top:425px"><div class="inner"><div class="state-name">Wien</div><svg class="corner"><use href="#click-corner"/></svg></div></a>
  </main>

  <footer class="site-footer">
    <div class="footer-col" style="left:278px">
      <h3>NAM VULPUTATE MAURIS</h3>
      <ul class="link-list">
        <li>Vivamus eu magna</li><li>Rhoncus</li><li>Consectetur metus</li>
        <li>Varius lacus</li><li>Donec ultricies</li><li>Tortor quis</li>
      </ul>
    </div>
    <div class="footer-col" style="left:512px">
      <h3>IN COMMODO EGESTAS</h3>
      <ul class="link-list">
        <li>Quisque adipiscing</li><li>Fusce quam dui</li><li>Vestibulum ante</li>
        <li>Duis sagittis</li><li>Mauris feugiat</li><li>Etiam sed mi</li>
      </ul>
    </div>
    <div class="footer-col" style="left:720px">
      <h3>FOLLOW US ON</h3>
      <ul class="social-list">
        <li><span class="social-icon"></span>Socialia</li>
        <li><span class="social-icon"></span>Chirper</li>
        <li><span class="social-icon"></span>Yodelnet</li>
      </ul>
    </div>
    <p class="copyright">Copyright © 2013 rohrwerk.at.</p>
  </footer>
</body>
</html>
```